Maple Crest - Marketing Flyer Q3 2017

Update: Added sample pics for half size paper flyer to give you an idea.

Need a flyer for dental clinic marketing. Attached the Grand Opening Specials flyer designs.

First page:
Replace the "Grand Opening Specials" section with below Offers and may be no heading
1. Back to School Specials!! $69
(Includes exam, cleaning, digital x-rays & fluoride)
2. Adults Exam & X-rays $49
3. Korvetrum FREE Consultation (see if you can use attached Korvetrum logo)

Second page:
Have below points under "Family & Cosmetic Dentistry".
1. Same day appointments
2. After hours support for emergencies
3. State-Of-The-Art equipment & digital facility
4. Affordable prices & flexible payment plans
5. Entertainment devices for patient comfort
6. We also speak Spanish

Pictures: one option is kids & female doctor (attached) in front page and family pic (attached) in back page.
Map: It should have a colorful frame similar to the attached original design.

Note: Need quick half page flyer design after approval of full page flyer. Will be mailing out the full page & half page flyers.
Updates

I need to wrap up the design by this Week end. Show off your innovative design skills and help with the new dental practice marketing!Thanks Added Friday, August 4, 2017

Target Market(s)

Kids and Teens

Industry/Entity Type

Dental

Colors

Designer to choose colors to be used in the design.

Requirements
Must have
• 1. Interesting Offers design
• 2. Innovative and Intriguing design layout
• 4. Organize the below key info accordingly
• - Company logo and name
• - Phone number [prominent space, refer in attached design]
• - Teeth shape
• - Offers
Nice to have
• A fresh new and better design than the previous attached design, which I've used it for the dental clinic opening.
Should not have
• - too many colors and font types
• - glaring colors and fonts

```html
<!DOCTYPE html>
<html lang="en">
<head>
<meta charset="utf-8">
<title>Maple Crest Dentistry – Back to School Flyer</title>
<link href="https://fonts.googleapis.com/css2?family=Fredoka:wght@500;600&family=Open+Sans:wght@400;600;700;800&display=swap" rel="stylesheet">
<style>
  :root{
    --navy:#2b5fae;
    --cyan:#1db3e8;
    --cyan-deep:#13a2d8;
    --ink:#151515;
    --paper:#ffffff;
    --backdrop:#eceae7;
    --frame-shadow:#c9ccd1;
  }
  *{box-sizing:border-box;margin:0;padding:0}
  html,body{width:1200px;height:864px;overflow:hidden;background:var(--backdrop)}
  body{font-family:"Open Sans",Arial,sans-serif;color:var(--ink)}
  .flyer{position:absolute;left:310px;top:22px;width:580px;height:820px;background:var(--paper);
    box-shadow:0 6px 22px rgba(0,0,0,.12);overflow:hidden}
  .flyer-bg{position:absolute;inset:0}
  .brand{position:absolute;left:34px;top:34px;display:flex;align-items:center;gap:14px}
  .brand-dot{width:44px;height:44px;border-radius:50%;background:var(--navy);flex:none}
  .brand-name{font-family:"Fredoka",sans-serif;font-weight:600;font-size:33px;color:var(--navy);line-height:1}
  .brand-tagline{font-family:"Open Sans",sans-serif;font-weight:700;font-size:15px;color:var(--cyan);margin-top:4px}
  .photo-frame{position:absolute;left:298px;top:72px;width:274px;height:334px}
  .offers{position:absolute;left:40px;top:170px;width:270px}
  .offer{font-weight:800;font-size:17px;line-height:1.15}
  .offer .price{color:var(--cyan);font-family:"Fredoka",sans-serif;font-weight:600;font-size:20px}
  .offer-note{font-size:8.5px;font-weight:600;margin-bottom:14px}
  .offer-adult{margin-bottom:14px}
  .partner{display:flex;align-items:center;gap:6px}
  .partner-dot{width:12px;height:12px;border-radius:50%;background:var(--navy)}
  .partner-name{font-weight:600;font-size:16px;color:var(--navy)}
  .partner-text{font-weight:800;font-size:16px}
  .call-label{position:absolute;left:96px;top:318px;font-family:"Fredoka",sans-serif;font-weight:500;font-size:21px;color:var(--navy)}
  .call-pill{position:absolute;left:40px;top:350px;width:258px;height:50px;border-radius:25px;background:var(--navy);
    display:flex;align-items:center;gap:10px;padding-left:14px;color:#fff}
  .call-icon{width:26px;height:26px;border:2px solid #fff;border-radius:50%;display:flex;align-items:center;justify-content:center}
  .call-number{font-family:"Fredoka",sans-serif;font-weight:600;font-size:32px;letter-spacing:.5px}
  .services-label{position:absolute;font-family:"Open Sans",sans-serif;font-weight:800;font-size:22px;color:#fff;white-space:nowrap;letter-spacing:.5px}
  .services-label.left{left:-36px;top:560px;transform:rotate(-90deg)}
  .services-label.right{left:488px;top:420px;transform:rotate(90deg)}
  .services{position:absolute;left:86px;top:430px;width:396px;height:180px;display:flex}
  .service-col{flex:1;display:flex;flex-direction:column;justify-content:space-around;align-items:center;border-left:2px solid rgba(255,255,255,.85)}
  .service-col:first-child{border-left:none}
  .service{display:flex;flex-direction:column;align-items:center;text-align:center;color:#fff;font-weight:700;font-size:10.5px;line-height:1.15;text-transform:uppercase}
  .service svg{width:26px;height:26px;margin-bottom:3px}
  .hours-pill{position:absolute;left:96px;top:620px;width:390px;height:36px;border-radius:18px;background:#fff;border:3px solid var(--navy);
    display:flex;align-items:center;justify-content:center;font-weight:800;font-size:15.5px;color:var(--navy)}
  .validity{position:absolute;left:0;right:0;top:664px;text-align:center;color:#fff;font-weight:700;font-size:12px}
  .welcome{position:absolute;left:0;right:0;top:682px;text-align:center;color:var(--navy);font-weight:800;font-size:19px}
  .footer-web{position:absolute;left:60px;top:778px;display:flex;align-items:center;gap:6px;font-weight:700;font-size:12.5px;color:var(--ink)}
  .footer-divider{position:absolute;left:300px;top:738px;width:2px;height:40px;background:var(--navy)}
  .footer-contact{position:absolute;left:330px;top:738px;font-weight:700;font-size:12.5px;line-height:1.6}
  .footer-contact div{display:flex;align-items:center;gap:6px}
  .mini-icon{width:12px;height:12px}
</style>
</head>
<body>
<svg width="0" height="0" style="position:absolute">
  <defs>
    <symbol id="tooth-icon" viewBox="0 0 26 26">
      <path d="M13 6C10 3 4 3 4 9c0 4 2 6 3 10 1 3 2 5 3 5s1.5-5 3-5 2 5 3 5 2-2 3-5c1-4 3-6 3-10 0-6-6-6-9-3z" fill="none" stroke="#fff" stroke-width="1.8" stroke-linejoin="round"/>
    </symbol>
    <symbol id="phone-icon" viewBox="0 0 24 24">
      <path d="M7 3l3 5-2 2c1 2 3 4 5 5l2-2 5 3-2 4C11 20 4 13 3 5z" fill="currentColor"/>
    </symbol>
    <clipPath id="tooth-clip">
      <path d="M137 44C104 16 40 10 26 64 14 118 40 168 54 226c10 46 14 84 36 84 22 0 24-64 47-64s25 64 47 64c22 0 26-38 36-84 14-58 40-108 28-162C234 10 170 16 137 44z"/>
    </clipPath>
  </defs>
</svg>

<main class="flyer">
  <svg class="flyer-bg" width="580" height="820" viewBox="0 0 580 820" aria-hidden="true">
    <path d="M22 128 C 120 108 220 104 310 88 L 310 94 C 220 112 120 120 22 138Z" fill="var(--navy)"/>
    <path d="M0 456 C 150 446 262 404 330 330 L 580 240 L 580 712 L 0 712 Z" fill="var(--cyan)"/>
    <path d="M0 456 C 150 446 262 404 330 330" fill="none" stroke="var(--navy)" stroke-width="5"/>
  </svg>

  <header class="brand">
    <div class="brand-dot"></div>
    <div>
      <div class="brand-name">Maple Crest Dentistry</div>
      <div class="brand-tagline">Modern Dental Care for All Ages</div>
    </div>
  </header>

  <svg class="photo-frame" viewBox="0 0 274 334">
    <path d="M137 34C100 4 30 -2 14 60 0 118 28 170 44 230c12 50 16 94 46 94 28 0 26-68 47-68s19 68 47 68c30 0 34-44 46-94 16-60 44-112 30-170C244 -2 174 4 137 34z" fill="var(--frame-shadow)"/>
    <path d="M137 38C102 8 34 2 19 62 5 118 33 168 48 228c11 48 15 88 42 88 25 0 25-66 47-66s22 66 47 66c27 0 31-40 42-88 15-60 43-110 29-166C240 2 172 8 137 38z" fill="#fff"/>
    <linearGradient id="photo-tones" x1="0" y1="0" x2="1" y2="1">
      <stop offset="0" stop-color="#f3f1f0"/>
      <stop offset=".5" stop-color="#e8c7b4"/>
      <stop offset="1" stop-color="#cfe6ec"/>
    </linearGradient>
    <rect x="0" y="0" width="274" height="334" fill="url(#photo-tones)" clip-path="url(#tooth-clip)" role="img" aria-label="Photo of a smiling young girl at a dental checkup, gloved hands holding dental tools"/>
  </svg>

  <section class="offers">
    <div class="offer">Back to School Specials!! <span class="price">$69</span></div>
    <div class="offer-note">(Includes exam, cleaning, digital x-rays &amp; fluoride)</div>
    <div class="offer offer-adult">Adults Exam &amp; X-rays <span class="price">$49</span></div>
    <div class="partner"><span class="partner-dot"></span><span class="partner-name">Korvetrum</span><span class="partner-text">FREE Consultation</span></div>
  </section>

  <div class="call-label">Call or Text Us Now:</div>
  <div class="call-pill">
    <span class="call-icon"><svg width="14" height="14" style="color:#fff"><use href="#phone-icon"/></svg></span>
    <span class="call-number">555.214.7380</span>
  </div>

  <div class="services-label left">OUR SERVICES</div>
  <div class="services-label right">OUR SERVICES</div>

  <section class="services">
    <div class="service-col">
      <div class="service"><svg><use href="#tooth-icon"/></svg>Root Canal<br>Therapy</div>
      <div class="service"><svg><use href="#tooth-icon"/></svg>Brightline Teeth<br>Whitening</div>
      <div class="service"><svg><use href="#tooth-icon"/></svg>Extractions</div>
    </div>
    <div class="service-col">
      <div class="service"><svg><use href="#tooth-icon"/></svg>Dentures</div>
      <div class="service"><svg><use href="#tooth-icon"/></svg>Implants</div>
      <div class="service"><svg><use href="#tooth-icon"/></svg>Veneers</div>
    </div>
    <div class="service-col">
      <div class="service"><svg><use href="#tooth-icon"/></svg>Korvetrum<br>(invisible braces)</div>
      <div class="service"><svg><use href="#tooth-icon"/></svg>Night Guards</div>
      <div class="service"><svg><use href="#tooth-icon"/></svg>Crown and<br>Bridge</div>
    </div>
  </section>

  <div class="hours-pill">CONVENIENT EVENING &amp; SATURDAY HOURS</div>
  <div class="validity">Opening special offers valid until June 15, 2017 by Appointment only</div>
  <div class="welcome">NEW PATIENTS ARE WELCOME!</div>

  <div class="footer-web">
    <svg class="mini-icon" viewBox="0 0 12 12"><circle cx="6" cy="6" r="5" fill="none" stroke="var(--navy)" stroke-width="1.4"/><path d="M1 6h10M6 1c-2 3-2 7 0 10M6 1c2 3 2 7 0 10" fill="none" stroke="var(--navy)" stroke-width="1"/></svg>
    www.MapleCrestDental.com
  </div>
  <div class="footer-divider"></div>
  <div class="footer-contact">
    <div><svg class="mini-icon" viewBox="0 0 12 12"><rect x="1" y="2.5" width="10" height="7" fill="none" stroke="var(--navy)" stroke-width="1.4"/><path d="M1 3l5 4 5-4" fill="none" stroke="var(--navy)" stroke-width="1.2"/></svg>info@MapleCrestDental.com</div>
    <div><svg class="mini-icon" style="color:var(--navy)"><use href="#phone-icon"/></svg>555-214-7380</div>
  </div>
</main>
</body>
</html>
```